DL Flyer for vehicle buying/selling service and advice business

New business to help people sell their current vehicle then select and buy and maintain their next car. (New or used).
We'll prepare and sell your car for you and get $,000s more than a trade in.
Offer advice as to the best car currently on the market based on our customer's needs.
With country wide sourcing network of cars across all manufacturers we have great buying power to ensure the very best possible price.
Personal service, including preparation of car for sale, pickup of old and drop-off of new vehicles, organise RWC and any required repairs.
We are NOT a car dealer so we WILL not try to sell you the vehicles we own.
Totally impartial, professional and friendly service making the purchase of your next car a great experience.
Updates

Flyer wording===========“Don’t sell your car or buy your next car without speaking to us”We guarantee to get you a better price for your current car and to find a cheaper purchase price for your next car.With a country wide sourcing network of cars “new and used” across all manufacturers we have sensational buying power to ensure the very best possible price.We can source the right car on any budget, from $2,000 to $200,000We are NOT a car dealer so we WILL not try to sell you the vehicles we own.By not being affiliated with any individual car manufacturer or dealer we can offer absolute impartiality.We’ll sit with you to discuss the best car for your needs and even bring the car to you for a test drive without the pressure of a salesperson nearby.Our services include:• Selling your current car: - Obtaining a roadworthy certificate - Organising any repairs needed - Detailing your car (wash, vacuum, polish) - Advertising of your car - Dealing with potential buyers - Negotiating the best price on your behalf• Assisting with the selection of your next car• Organising test drives• Purchasing the car of your choice - Sourcing the very best price• Ongoing management of their vehicle (service, clean, repair)Possible inclusions in the flyer might be:Advantages of upgrading to a new vehicle include:o reliability, o safety,o fuel efficiencyo comfort.Space for a couple of short testimonials Background images of all of the major car manufacturers Added Friday, July 29, 2016

Target Market(s)

Local community.
Initially will drop DL flyers in local post boxes

Industry/Entity Type

Business

Requirements
Must have
• Flyer wording:
• ===========
• “Don’t sell your car or buy your next car without speaking to us”
• ---------------------------------------------------------------------------------
• We guarantee to get you a better price for your current car and to find a cheaper purchase price for your next car.
• With a country wide sourcing network of cars “new and used” across all manufacturers we have sensational buying power to ensure the very best possible price.
• We can source the right car on any budget, from $2,000 to $200,000
• We are NOT a car dealer so we WILL not try to sell you the vehicles we own.
• By not being affiliated with any individual car manufacturer or dealer we can offer absolute impartiality.
• We’ll sit with you to discuss the best car for your needs and even bring the car to you for a test drive without the pressure of a salesperson nearby.
• Our services include:
• • Selling your current car:
• o Obtaining a roadworthy certificate
• o Organising any repairs needed
• o Detailing your car (wash, vacuum, polish)
• o Advertising of your car
• o Dealing with potential buyers
• o Negotiating the best price on your behalf
• • Assisting with the selection of your next car
• • Organising test drives
• • Purchasing the car of your choice
• o Sourcing the very best price
• • Ongoing management of your vehicle (service, clean, repair)
• Call Gerald on: 0427 315064
Nice to have
• Possible inclusions on the flyer might be:
• List of advantages of upgrading to a new vehicle:
• o reliability,
• o safety,
• o fuel efficiency
• o comfort
• Space for a couple of short testimonials
• Background images of all of the major car manufacturers

```html
<!DOCTYPE html>
<html lang="en">
<head>
<meta charset="utf-8">
<title>TBA – DL Flyer</title>
<link rel="stylesheet" href="https://fonts.googleapis.com/css2?family=Bebas+Neue&family=Roboto+Condensed:ital,wght@0,700;1,700&family=Open+Sans:wght@400;700&family=Oswald:wght@500;600&display=swap">
<style>
  :root {
    --backdrop: #3a3a3c;
    --red: #d81c24;
    --red-deep: #a8141b;
    --ink: #231f20;
    --charcoal: #2b2b2d;
    --paper: #ffffff;
    --paper-grey: #e4e4e4;
    --photo-sky: #8fb4d6;
    --photo-silver: #c9ccd0;
    --photo-warm: #b59a84;
  }
  * { box-sizing: border-box; margin: 0; padding: 0; }
  html, body { width: 1200px; height: 900px; overflow: hidden; }
  body { background: var(--backdrop); position: relative; font-family: "Open Sans", sans-serif; }

  .flyer { position: absolute; top: 58px; width: 381px; height: 782px; overflow: hidden; background: var(--paper); }
  .flyer--front { left: 160px; }
  .flyer--back { left: 635px; }
  .flyer-shapes { position: absolute; inset: 0; }

  /* Front */
  .headline { position: absolute; top: 30px; left: 0; width: 100%; text-align: center; font-family: "Bebas Neue", sans-serif; line-height: .95; color: var(--ink); }
  .headline__line1 { font-size: 34px; }
  .headline__line2 { font-size: 52px; }
  .headline__line3 { font-size: 40px; color: var(--red); }

  .benefits { position: absolute; top: 446px; left: 38px; width: 320px; list-style: none; font-family: "Roboto Condensed", sans-serif; font-style: italic; font-weight: 700; font-size: 10.4px; line-height: 14.5px; color: var(--paper); }
  .benefits li { position: relative; padding-left: 16px; margin-bottom: 9px; }
  .benefits li::before { content: ""; position: absolute; left: 0; top: 4px; width: 7px; height: 7px; border-radius: 50%; background: var(--paper); }

  .brand-bar { position: absolute; left: 0; top: 672px; width: 100%; height: 80px; display: flex; align-items: center; }
  .brand-name { width: 110px; text-align: center; font-family: "Oswald", sans-serif; font-weight: 600; font-size: 34px; color: var(--red); border-right: 2px solid var(--ink); line-height: 44px; }
  .advantages { display: grid; grid-template-columns: auto auto; gap: 8px 14px; margin-left: 20px; font-family: "Oswald", sans-serif; font-weight: 600; font-size: 13px; color: var(--red); }
  .advantage { display: flex; align-items: center; gap: 6px; }
  .advantage svg { width: 20px; height: 22px; }

  /* Back */
  .services { position: absolute; top: 245px; left: 38px; width: 330px; color: var(--paper); }
  .services__title { font-family: "Oswald", sans-serif; font-weight: 500; font-size: 22px; letter-spacing: .3px; margin-bottom: 10px; }
  .services__list { list-style: none; font-weight: 700; font-size: 11.6px; line-height: 16px; }
  .services__list > li { position: relative; padding-left: 18px; margin-bottom: 4px; }
  .services__list > li::before { content: ""; position: absolute; left: 2px; top: 4px; width: 7px; height: 7px; background: var(--paper); transform: rotate(45deg); }
  .services__sub { list-style: none; margin-top: 1px; }
  .services__sub li { position: relative; padding-left: 20px; }
  .services__sub li::before { content: ""; position: absolute; left: 6px; top: 5px; width: 6px; height: 6px; border-radius: 50%; background: var(--paper); }

  .testimonial { position: absolute; top: 566px; width: 130px; text-align: center; font-size: 8.2px; line-height: 11.5px; color: var(--paper); }
  .testimonial--one { left: 33px; }
  .testimonial--two { left: 196px; }
  .testimonial__mark { display: block; font-family: "Oswald", sans-serif; font-size: 22px; line-height: 18px; color: var(--red); margin-bottom: 4px; }

  .call { position: absolute; top: 714px; width: 100%; text-align: center; font-family: "Oswald", sans-serif; font-weight: 500; font-size: 22px; color: var(--red); }
  .website { position: absolute; top: 748px; width: 100%; text-align: center; font-size: 15px; letter-spacing: 2px; color: var(--ink); }
</style>
</head>
<body>

<section class="flyer flyer--front">
  <svg class="flyer-shapes" viewBox="0 0 381 782" aria-hidden="true">
    <defs>
      <linearGradient id="front-paper" x1="0" y1="0" x2="0" y2="1">
        <stop offset="0" stop-color="#f4f4f4"/><stop offset="1" stop-color="#dcdcdc"/>
      </linearGradient>
      <radialGradient id="front-red" cx=".5" cy=".35" r=".8">
        <stop offset="0" stop-color="#e3262e"/><stop offset="1" stop-color="#a8141b"/>
      </radialGradient>
      <linearGradient id="front-photo" x1="0" y1="0" x2="1" y2="1">
        <stop offset="0" stop-color="#8fb4d6"/><stop offset=".5" stop-color="#c9ccd0"/><stop offset="1" stop-color="#b59a84"/>
      </linearGradient>
    </defs>
    <rect width="381" height="672" fill="url(#front-paper)"/>
    <polygon points="0,408 381,372 381,672 0,672" fill="url(#front-red)"/>
    <polygon points="0,203 62,176 381,176 381,190 68,190 0,217" fill="#231f20"/>
    <polygon points="0,196 58,171 381,171 381,178 60,178 0,204" fill="#d81c24"/>
    <polygon points="0,420 296,420 381,386 381,398 300,432 0,432" fill="#ffffff"/>
    <polygon points="0,412 292,412 381,376 381,386 296,420 0,420" fill="#231f20"/>
  </svg>
  <svg class="flyer-shapes" viewBox="0 0 381 782" role="img" aria-label="Photo: a couple talking with a car adviser beside a silver car outside a dealership">
    <polygon points="0,217 68,190 381,190 381,376 292,412 0,412" fill="url(#front-photo)"/>
  </svg>

  <h1 class="headline">
    <span class="headline__line1">Don’t sell your car or</span><br>
    <span class="headline__line2">Buy your next car</span><br>
    <span class="headline__line3">Without speaking to us</span>
  </h1>

  <ul class="benefits">
    <li>We guarantee to get you a better price for your current car and to find a cheaper purchase price for your next car.</li>
    <li>With a country wide sourcing network of cars “new and used” across all manufacturers we have sensational buying power to ensure the very best possible price.</li>
    <li>We can source the right car on any budget, from $2,000 to $200,000</li>
    <li>We are NOT a car dealer so we WILL not try to sell you the vehicles we own.</li>
    <li>By not being affiliated with any individual car manufacturer or dealer we can offer absolute impartiality.</li>
    <li>We’ll sit with you to discuss the best car for your needs and even bring the car to you for a test drive without the pressure of a salesperson nearby.</li>
  </ul>

  <div class="brand-bar">
    <div class="brand-name">TBA</div>
    <div class="advantages">
      <span class="advantage"><svg viewBox="0 0 20 22" aria-hidden="true"><polygon points="10,0 20,5.5 20,16.5 10,22 0,16.5 0,5.5" fill="#231f20"/><path d="M5 11 L8.5 14.5 L15 7.5" stroke="#fff" stroke-width="2" fill="none"/></svg>Reliability</span>
      <span class="advantage"><svg viewBox="0 0 20 22" aria-hidden="true"><polygon points="10,0 20,5.5 20,16.5 10,22 0,16.5 0,5.5" fill="#231f20"/><path d="M10 5 C8 9 6 11 6 13.5 A4 4 0 0 0 14 13.5 C14 11 12 9 10 5Z" fill="#fff"/></svg>Fuel efficiency</span>
      <span class="advantage"><svg viewBox="0 0 20 22" aria-hidden="true"><polygon points="10,0 20,5.5 20,16.5 10,22 0,16.5 0,5.5" fill="#231f20"/><path d="M10 15.5 L15 7.5 H5 Z" fill="#fff"/></svg>Safety</span>
      <span class="advantage"><svg viewBox="0 0 20 22" aria-hidden="true"><polygon points="10,0 20,5.5 20,16.5 10,22 0,16.5 0,5.5" fill="#231f20"/><rect x="5" y="12" width="10" height="4" fill="#fff"/><rect x="6" y="7" width="3" height="5" fill="#fff"/></svg>Comfort</span>
    </div>
  </div>
  <svg class="flyer-shapes" viewBox="0 0 381 782" aria-hidden="true"><rect y="752" width="381" height="30" fill="#2b2b2d"/></svg>
</section>

<section class="flyer flyer--back">
  <svg class="flyer-shapes" viewBox="0 0 381 782" aria-hidden="true">
    <defs>
      <linearGradient id="back-photo" x1="0" y1="0" x2="1" y2="0">
        <stop offset="0" stop-color="#b59a84"/><stop offset=".6" stop-color="#c9ccd0"/><stop offset="1" stop-color="#e6e8ea"/>
      </linearGradient>
      <radialGradient id="back-red" cx=".5" cy=".3" r=".85">
        <stop offset="0" stop-color="#e3262e"/><stop offset="1" stop-color="#a8141b"/>
      </radialGradient>
      <linearGradient id="back-foot" x1="0" y1="0" x2="0" y2="1">
        <stop offset="0" stop-color="#ffffff"/><stop offset="1" stop-color="#e0e0e0"/>
      </linearGradient>
    </defs>
    <rect width="381" height="682" fill="url(#back-red)"/>
    <polygon points="0,210 268,210 381,312 381,326 262,222 0,222" fill="#231f20"/>
    <polygon points="0,222 262,222 381,326 381,334 258,230 0,230" fill="#ffffff"/>
    <rect y="682" width="381" height="100" fill="url(#back-foot)"/>
    <polygon points="18,546 168,546 158,694 8,694" fill="#ffffff"/>
    <polygon points="21,549 165,549 155,691 11,691" fill="#231f20"/>
    <polygon points="184,546 360,546 360,694 174,694" fill="#ffffff"/>
    <polygon points="187,549 357,549 357,691 177,691" fill="#231f20"/>
  </svg>
  <svg class="flyer-shapes" viewBox="0 0 381 782" role="img" aria-label="Photo: a smiling family holding car keys beside a new white car">
    <polygon points="0,0 381,0 381,312 268,210 0,210" fill="url(#back-photo)"/>
  </svg>

  <div class="services">
    <h2 class="services__title">OUR SERVICES</h2>
    <ul class="services__list">
      <li>Selling your current car:
        <ul class="services__sub">
          <li>Obtaining a roadworthy certificate</li>
          <li>Organising any repairs needed</li>
          <li>Detailing your car (wash, vacuum, polish)</li>
          <li>Advertising of your car</li>
          <li>Dealing with potential buyers</li>
          <li>Negotiating the best price on your behalf</li>
        </ul>
      </li>
      <li>Assisting with the selection of your next car</li>
      <li>Organising test drives</li>
      <li>Purchasing the car of your choice
        <ul class="services__sub"><li>Sourcing the very best price</li></ul>
      </li>
      <li>Ongoing management of your vehicle (service, clean, repair)</li>
    </ul>
  </div>

  <blockquote class="testimonial testimonial--one">
    <span class="testimonial__mark">“”</span>
    Lorem ipsum dolor sit amet, consectetur adipiscing elit. Vestibulum et dapibus neque. Cras a massa ex. Sed elit sem, dapibus ac volutpat ut, aliquet in tortor. Nam gravida quam sed ligula aliquam, nec aliquam urna ultricies.
  </blockquote>
  <blockquote class="testimonial testimonial--two">
    <span class="testimonial__mark">“”</span>
    Lorem ipsum dolor sit amet, consectetur adipiscing elit. Vestibulum et dapibus neque. Cras a massa ex. Sed elit sem, dapibus ac volutpat ut, aliquet in tortor. Nam gravida quam sed ligula aliquam, nec aliquam urna ultricies.
  </blockquote>

  <p class="call">CALL US AT XXX-XXX-XXXX</p>
  <p class="website">www.yourwebsite.com</p>
</section>

</body>
</html>
```